Therapeutic Counselling Practice Brochure

I have a new therapeutic counselling practice in Melbourne.

I am making peri natal issues my special interest area.

I need a brochure targeted at new parents or pregnant women and partners, struggling with the concept of parenting, depression, maybe do not even know about it.

The feel should be safe and strong. I love the KOALIN website ( I do volunteer work with them)

Out of hours appointments and telephone counselling are important making my service very accessible.

Attached is an example for the content of the Brochure
Updates

Attached is an example for the content of the Brochure.

Target Market(s)

25 - 45 New Parents , expectant parents,families and friends of people struggling emotionally and mentally with and around being new parents

Industry/Entity Type

Work

Requirements
Must have
• Feel of safety, somewhere to go for help, support, a conversation, soft ,strong
Nice to have
• mother and child, maybe parents and child, possibly a graphic, faceless

```html
<!DOCTYPE html>
<html lang="en">
<head>
<meta charset="utf-8">
<title>Helena Marsh – Perinatal Counselling Brochure</title>
<link rel="stylesheet" href="https://fonts.googleapis.com/css2?family=Lobster&family=Oswald:wght@500;600&family=Pathway+Gothic+One&display=swap">
<style>
  :root {
    --sky: #8dd0de;
    --sky-deep: #79c9d6;
    --sky-band: #68b6c3;
    --slate: #939598;
    --rose: #e5506f;
    --rose-soft: #f3c4cf;
    --ink: #6d6e70;
    --ink-soft: #7f8082;
    --paper: #ffffff;
    --rule: #b9bbbd;
  }
  * { margin: 0; padding: 0; box-sizing: border-box; }
  html, body { width: 1200px; height: 900px; overflow: hidden; background: var(--paper); }
  body { position: relative; font-family: "Pathway Gothic One", "Arial Narrow", sans-serif; color: var(--ink); }

  .brochure {
    position: absolute; left: 73px; top: 80px; width: 1054px; height: 740px;
    box-shadow: 2px 3px 6px rgba(0,0,0,.28);
    display: flex;
  }
  .panel { position: relative; height: 100%; overflow: hidden; }
  .panel p, .panel h1, .panel h2, .panel h3, .panel h4 { white-space: nowrap; }

  /* Left panel */
  .panel--fathers { width: 352px; background: var(--paper); }
  .panel--fathers::after {
    content: ""; position: absolute; right: 0; top: 0; width: 40px; height: 100%;
    background: linear-gradient(to right, rgba(0,0,0,0), rgba(0,0,0,.07));
  }
  .fathers__block { position: absolute; left: 26px; }
  .fathers__title { top: 52px; font-family: "Lobster", cursive; font-weight: 400; color: var(--sky); font-size: 41px; line-height: 1; }
  .fathers__subtitle { top: 100px; font-family: "Lobster", cursive; font-weight: 400; color: var(--sky); font-size: 24px; line-height: 1.1; }
  .fathers__copy { font-size: 13.5px; line-height: 19px; color: var(--ink-soft); }
  .fathers__copy p + p { margin-top: 4px; }
  .fathers__stat { top: 206px; font-size: 20px; line-height: 24px; color: var(--sky); }
  .fathers__stat strong { font-family: "Oswald", sans-serif; font-weight: 600; font-size: 17px; }
  .fathers__source { top: 278px; right: 26px; left: auto; font-family: "Lobster", cursive; font-size: 10px; color: var(--sky); }
  .fathers__pullquote { top: 414px; font-size: 20px; line-height: 24px; color: var(--sky); }

  /* Middle panel */
  .panel--contact { width: 350px; background: var(--slate); color: var(--paper); text-align: center; }
  .portrait {
    position: absolute; left: 25px; top: 55px; width: 300px; height: 221px;
    border: 4px solid var(--rose); padding: 3px; background: var(--paper);
  }
  .portrait__fill { width: 100%; height: 100%; background: linear-gradient(110deg, #c9b08f 0%, #b98e6e 40%, #5e7a3c 80%, #3f5a2a 100%); }
  .contact__name { position: absolute; top: 290px; width: 100%; font-family: "Oswald", sans-serif; font-weight: 600; font-size: 17px; line-height: 1.2; }
  .contact__heading { font-family: "Lobster", cursive; font-weight: 400; color: var(--sky); font-size: 20px; line-height: 26px; }
  .contact__office { position: absolute; top: 328px; width: 100%; font-size: 15px; line-height: 20px; }
  .contact__phone-info { position: absolute; top: 410px; width: 100%; font-size: 13.5px; line-height: 19px; }
  .booking {
    position: absolute; left: 0; bottom: 0; width: 100%; height: 165px;
    background: var(--sky-deep); border-top: 12px solid var(--sky-band); padding-top: 16px;
  }
  .booking__title { font-family: "Oswald", sans-serif; font-weight: 500; font-size: 17px; line-height: 1.3; }
  .booking__lines { font-size: 15px; line-height: 20px; margin-top: 8px; }
  .booking__web { font-family: "Oswald", sans-serif; font-weight: 600; font-size: 17px; margin-top: 6px; }

  /* Right panel */
  .panel--cover { width: 352px; background: var(--paper); }
  .cover__header { height: 154px; background: var(--sky); color: var(--paper); text-align: center; padding-top: 32px; border-bottom: 4px solid var(--rule); }
  .cover__kicker { font-family: "Lobster", cursive; font-weight: 400; font-size: 32px; line-height: 1; }
  .cover__title { font-family: "Lobster", cursive; font-weight: 400; font-size: 54px; line-height: 1.1; }
  .cover__art { position: absolute; left: 0; top: 154px; }
  .badge {
    position: absolute; left: 11px; top: 442px; width: 152px; height: 152px; border-radius: 50%;
    background: var(--rose); border: 3px solid var(--paper); box-shadow: 0 0 0 1px rgba(0,0,0,.08);
    color: var(--paper); text-align: center; padding-top: 44px;
  }
  .badge__name { font-family: "Oswald", sans-serif; font-weight: 600; font-size: 17px; line-height: 1.2; }
  .badge__role { font-family: "Oswald", sans-serif; font-weight: 500; font-size: 11px; line-height: 1.3; }
  .badge__phone { font-family: "Oswald", sans-serif; font-weight: 600; font-size: 17px; margin-top: 5px; }
  .cover__intro { position: absolute; left: 25px; top: 598px; font-size: 15px; line-height: 19px; color: var(--ink); }
  .cover__intro p + p { margin-top: 5px; }
  .cover__mark { position: absolute; left: 256px; top: 568px; width: 60px; height: 108px; border-radius: 30px; background: var(--rose-soft); }
</style>
</head>
<body>
  <div class="brochure">
    <section class="panel panel--fathers">
      <h2 class="fathers__block fathers__title">Depression in Men</h2>
      <p class="fathers__block fathers__subtitle">after the birth of their Baby</p>

      <div class="fathers__block fathers__copy" style="top:162px">
        <p>Becoming a father can be difficult to cope with and some men<br>feel they have nowhere to turn for support.</p>
      </div>
      <p class="fathers__block fathers__stat">According to recent research,<br><strong>about 10% of new fathers</strong> become<br>depressed after the birth of their child.</p>
      <p class="fathers__block fathers__source">www.parentmind.org.uk</p>
      <div class="fathers__block fathers__copy" style="top:298px">
        <p>Having a new baby is a huge change, involving physical<br>exhaustion and extra worries.</p>
        <p>It can be particularly difficult to balance the demands of work<br>and fatherhood, especially as you might feel under pressure to<br>earn more while your partner is not able to work.</p>
      </div>
      <p class="fathers__block fathers__pullquote">For new parents the focus of attention<br>will have shifted and this can feel like<br>a loss as well as a gain.</p>
      <div class="fathers__block fathers__copy" style="top:502px">
        <p>Some men report feeling overwhelmed, isolated and confused<br>by their feelings and their partner's reaction to them. They are<br>often irritable, aggressive and sometimes hostile.</p>
        <p>Symptoms can include feeling very low - for example, not<br>enjoying anything, poor concentration, perhaps a poor appetite<br>and worrying at night.</p>
        <p>Some men feel ashamed of their feelings and experiences and<br>this makes it very difficult for them to seek out and receive help.</p>
        <p>Counselling can help, being able to talk openly and honestly<br>in a safe and confidential space.</p>
      </div>
    </section>

    <section class="panel panel--contact">
      <div class="portrait"><div class="portrait__fill" role="img" aria-label="Portrait photograph of the counsellor in front of green foliage"></div></div>
      <h3 class="contact__name">Helena Marsh J.P.</h3>
      <div class="contact__office">
        <h4 class="contact__heading">Office:</h4>
        <p>Level 1, 48 Harbour Lane, Southbank 3006<br>Evening and weekend appointments available.</p>
      </div>
      <div class="contact__phone-info">
        <h4 class="contact__heading">Telephone Counselling:</h4>
        <p>Some people feel more comfortable discussing issues over<br>the telephone, still within the safe supportive and confidential<br>framework. It can be a convenient option in accessing therapy,<br>saveing travel time and the hassle of parking. Telephone<br>appointments are usually available within 48 hours.</p>
      </div>
      <div class="booking">
        <p class="booking__title">To book please contact...</p>
        <p class="booking__lines">Helena Marsh on 0400 555 018<br>helena@helenamarsh.com.au</p>
        <p class="booking__web">www.helenamarsh.com.au</p>
      </div>
    </section>

    <section class="panel panel--cover">
      <header class="cover__header">
        <p class="cover__kicker">Have you got the</p>
        <h1 class="cover__title">‘Baby Blues’?</h1>
      </header>
      <svg class="cover__art" width="352" height="586" viewBox="0 0 352 586">
        <defs>
          <linearGradient id="artWash" x1="0" y1="0" x2="1" y2="1">
            <stop offset="0" stop-color="#b9c9cf"/>
            <stop offset=".45" stop-color="#b07a4e"/>
            <stop offset=".75" stop-color="#d9c2a8"/>
            <stop offset="1" stop-color="#9ccbd6"/>
          </linearGradient>
        </defs>
        <rect width="352" height="440" fill="url(#artWash)" role="img" aria-label="Watercolour illustration of a young mother with long brown hair looking down"/>
        <path d="M0 432 Q170 420 352 326 L352 586 L0 586 Z" fill="#ffffff"/>
      </svg>
      <div class="badge">
        <p class="badge__name">Helena Marsh</p>
        <p class="badge__role">Counsellor &amp; Personal Coach</p>
        <p class="badge__phone">0400 555 018</p>
      </div>
      <div class="cover__intro">
        <p>There is an expectation of happiness<br>and fulfilment around childbirth.</p>
        <p>Feeling ‘blue’ interferes with the<br>adjustment to becoming a parent.</p>
        <p>Sharing your feelings by talking is important.</p>
      </div>
      <div class="cover__mark" role="img" aria-label="Line drawing of a mother holding a child"></div>
    </section>
  </div>
</body>
</html>
```